Web Design Project

We wish to create a web based logistics exchange for heavy machinery and equipment catering to the mining, oil, gas and infrastructure industries. Customers interested in shipping equipment can post a load on the site and this would then be auctioned off through an online auction to prospective transport providers.Payments would be through direct bank transfer,zenu, plumtender etc.
Both shippers and transport providers gain access via membership.
When a load is posted it would appear on the map indicating its location.Transport providers click on the icon of this map to access information of the pick up and delivery details as well as the load description.
The site would also have links to transport departments and equipment specification sites.
Advertising and merchandising are the other areas of revenue through the site

Target Market(s)

Shippers from Machinery Auction centres and Transport companies

Industry/Entity Type

Catering

Requirements
Must have
• The Logo of the company. The file is attached.

```html
<!DOCTYPE html>
<html lang="en">
<head>
<meta charset="utf-8">
<title>Velmorra Freight</title>
<link href="https://fonts.googleapis.com/css2?family=Jura:wght@500;600&family=Ubuntu:wght@400;500&display=swap" rel="stylesheet">
<style>
:root{
  --blue:#0a4a96;
  --blue-bright:#1a78c8;
  --ink:#333;
  --link:#1f4f8c;
  --grey-line:#d8d8d8;
  --footer-top:#0c3b7b;
  --footer-bottom:#2f5d97;
}
*{margin:0;padding:0;box-sizing:border-box}
html,body{width:1200px;height:900px;overflow:hidden;background:#fff}
body{position:relative;font-family:"Ubuntu",sans-serif;color:var(--ink);font-size:9px;line-height:11.1px}
.abs{position:absolute}
.display{font-family:"Jura",sans-serif;font-weight:600}

.brand{left:280px;top:26px;display:flex;align-items:center;gap:10px}
.brand-mark{width:36px;height:36px;background:var(--blue-bright)}
.brand-name{font-size:26px;color:#333;letter-spacing:.5px}
.account{left:779px;top:28px;font-size:10px;color:var(--link)}
.account span{margin:0 5px;color:#999}
.search{left:779px;top:51px;width:124px;height:18px;border:1px solid #7a9cc4;border-radius:4px}
.search-icon{left:906px;top:52px}

.nav{left:0;top:92px;width:1200px;height:27px;background:linear-gradient(#fafafa,#e9e9e9);border-top:1px solid #ddd;border-bottom:1px solid #cfcfcf}
.nav ul{list-style:none;position:absolute;left:279px;top:0;display:flex;height:100%}
.nav li{font-size:11px;color:var(--link);line-height:26px;text-align:center;border-right:1px solid #d2d2d2}
.nav li:last-child{border-right:0}

.hero{left:0;top:119px;width:1200px;height:183px;background:linear-gradient(180deg,#6fb7e6 0%,#a9d6ee 45%,#8fa0a8 62%,#4d6a8a 78%,#29406a 100%)}
.band{left:0;top:302px;width:1200px;height:23px;background:linear-gradient(#3d8fd6,#0f5aa8)}
.band-label{top:308px;font-size:10.5px;color:#fff;letter-spacing:.3px}

.tiles{left:279px;top:325px;width:644px;height:100px;border:1px solid var(--grey-line);border-top:0;border-radius:0 0 4px 4px;background:linear-gradient(#fff,#f1f1f1);display:flex}
.tile{position:relative;padding:13px 14px;border-right:1px solid var(--grey-line)}
.tile:last-child{border-right:0}
.tile p{width:186px}
.tile h3{font-size:12px;font-weight:500;margin-bottom:11px;color:#444}
.tile ul{list-style:none}
.tile li:before{content:"• "}
.more{position:absolute;right:16px;bottom:8px;font-size:10px;color:var(--link)}

.welcome{left:279px;top:438px;width:415px}
.welcome h1{font-size:16.5px;line-height:18px;color:var(--blue);font-weight:600;margin-bottom:10px}
.welcome h2{font-size:10px;color:var(--link);font-weight:500;margin-top:10px;line-height:12px}

.map{left:708px;top:437px;width:215px;height:81px;border-radius:4px;background:linear-gradient(135deg,#f2e6c6,#e9d7a5 45%,#c7d8e6);overflow:hidden}
.map-label{position:absolute;left:0;bottom:0;width:100%;height:28px;background:rgba(120,170,220,.75);color:#fff;font-size:11.5px;padding:8px 12px}
.panel{left:708px;width:215px;border-radius:4px;color:#fff;padding:11px 14px}
.panel h3{font-size:11.5px;font-weight:500;letter-spacing:.5px;padding-bottom:8px;border-bottom:1px solid #9fb9db;margin-bottom:10px}
.news{top:523px;height:139px;background:linear-gradient(#28579a,#0b3b7c)}
.news p{font-size:9.5px;line-height:11.3px}
.news small{display:block;font-size:7.5px;line-height:9px;color:#8faad4;margin-bottom:12px}
.newsletter{top:667px;height:77px;background:linear-gradient(#2a86d0,#0f5db0)}
.newsletter input{position:absolute;left:14px;top:45px;width:122px;height:19px;border:0;border-radius:3px;background:#fff}
.signup{position:absolute;left:145px;top:45px;width:54px;height:19px;border-radius:4px;background:linear-gradient(#fff,#c9d3df);color:var(--link);font-size:10px;text-align:center;line-height:19px;letter-spacing:.5px}

.footer{left:0;top:757px;width:1200px;height:143px;background:linear-gradient(var(--footer-top),var(--footer-bottom))}
.fcol{top:772px;color:#fff;width:180px}
.fcol h4{font-size:11.5px;font-weight:500;letter-spacing:.5px;padding-bottom:8px;border-bottom:1px solid #9fb6d4;margin-bottom:9px}
.fcol li{list-style:none;font-size:9.5px;line-height:15.3px;letter-spacing:.3px}
.social{left:791px;top:776px;display:flex;gap:4px}
.social span{width:23px;height:23px;background:#6b6f76}
.copy{left:827px;top:815px;font-size:9.5px;color:#fff}
</style>
</head>
<body>
<header>
  <div class="abs brand"><span class="brand-mark"></span><span class="brand-name display">VELMORRA</span></div>
  <div class="abs account">SIGN IN<span>|</span>REGISTER</div>
  <div class="abs search"></div>
  <svg class="abs search-icon" width="16" height="16" viewBox="0 0 16 16"><circle cx="6" cy="6" r="4.5" fill="none" stroke="#888" stroke-width="1.5"/><line x1="9.3" y1="9.3" x2="14.5" y2="14.5" stroke="#666" stroke-width="2.2"/></svg>
</header>

<nav class="abs nav">
  <ul class="display">
    <li style="width:72px">HOME</li><li style="width:88px">ABOUT US</li><li style="width:78px">CLIENTS</li><li style="width:79px">REPORTS</li><li style="width:83px">SERVICES</li><li style="width:80px">SUPPORT</li><li style="width:65px">MAP</li><li style="width:92px">CONTACT US</li>
  </ul>
</nav>

<div class="abs hero" role="img" aria-label="Photo of a white semi-trailer truck driving along a motorway under a blue sky"></div>
<div class="abs band"></div>
<div class="abs band-label display" style="left:292px">WHY VELMORRA?</div>
<div class="abs band-label display" style="left:507px">WHAT IS VELMORRA?</div>
<div class="abs band-label display" style="left:723px">WHAT OUR CLIENTS SAY</div>

<section class="abs tiles">
  <div class="tile" style="width:214px">
    <h3 class="display">SAVE TIME, SAVE MONEY</h3>
    <ul><li>Sed ut perspiciatis.</li><li>Nemo enim ipsam.</li><li>Neque porro quisquam.</li><li>Ut enim ad minima.</li></ul>
    <span class="more display">READ MORE</span>
  </div>
  <div class="tile" style="width:214px">
    <p>Ut enim ad minima veniam, quis nostrum exercitationem ullam corporis suscipit laboriosam, nisi ut aliquid ex ea commodi consequatur? Quis autem vel eum iure reprehenderit qui in ea fugiat quo voluptas nulla pariatur...</p>
    <span class="more display">READ MORE</span>
  </div>
  <div class="tile" style="width:214px">
    <p>Effortless. All of the tools you need to manage the most challenging aspect of any business. I have turned to VELMORRA for valuable information on how to...</p>
    <span class="more display">READ MORE</span>
  </div>
</section>

<main class="abs welcome">
  <h1 class="display">WELCOME TO VELMORRA<br>THE ONLY FREIGHT MANAGEMENT<br>SOLUTION YOU WILL EVER NEED</h1>
  <p>Sed ut perspiciatis unde omnis iste natus error sit voluptatem accusantium doloremque laudantium, totam rem aperiam, eaque ipsa quae ab illo inventore veritatis et quasi architecto beatae vitae dicta sunt explicabo. Nemo enim ipsam voluptatem quia voluptas sit aspernatur aut odit aut fugit, sed quia consequuntur magni dolores eos qui ratione voluptatem sequi nesciunt.</p>
  <h2 class="display">WHAT WE DO</h2>
  <p>Neque porro quisquam est, qui dolorem ipsum quia dolor sit amet, consectetur, adipisci velit, sed quia non numquam eius modi tempora incidunt ut labore et dolore magnam aliquam quaerat voluptatem. Ut enim ad minima veniam, quis nostrum exercitationem ullam corporis suscipit laboriosam, nisi ut aliquid ex ea commodi consequatur? Quis autem vel eum iure reprehenderit qui in ea voluptate velit esse quam nihil molestiae consequatur, vel illum qui dolorem eum fugiat quo voluptas nulla pariatur?</p>
  <h2 class="display">HOW TO JOIN</h2>
  <p>Ut enim ad minima veniam, quis nostrum exercitationem ullam corporis suscipit laboriosam, nisi ut aliquid ex ea commodi consequatur? Quis autem vel eum iure reprehenderit qui in ea voluptate velit esse quam nihil molestiae consequatur.</p>
  <h2 class="display">REPORT</h2>
  <p>Nemo enim ipsam voluptatem quia voluptas sit aspernatur aut odit aut fugit, sed quia consequuntur magni dolores eos qui ratione voluptatem sequi nesciunt.</p>
</main>

<aside>
  <div class="abs map" role="img" aria-label="Street map of a city area showing roads and suburbs">
    <div class="map-label display">INTERACTIVE MAP</div>
  </div>
  <div class="abs panel news">
    <h3 class="display">LATEST NEWS</h3>
    <p>August 2012 Newsletter.</p><small>READ MORE</small>
    <p>VELMORRA forms Strategic Relationship...</p><small>READ MORE</small>
    <p>VELMORRA signs new high profile client...</p><small>READ MORE</small>
  </div>
  <div class="abs panel newsletter">
    <h3 class="display">SIGN UP FOR OUR NEWSLETTER</h3>
    <input type="text" aria-label="Email address">
    <span class="signup display">SIGN UP</span>
  </div>
</aside>

<footer class="abs footer"></footer>
<div class="abs fcol" style="left:286px">
  <h4 class="display">INFORMATION</h4>
  <ul><li>Terms &amp; Conditions</li><li>Frequently Asked Questions</li></ul>
</div>
<div class="abs fcol" style="left:507px">
  <h4 class="display">AFFILIATES</h4>
  <ul><li>Quis Autem</li><li>Nemoenim</li><li>Sedquia</li><li>Fugiat</li><li>Magni Dolores</li></ul>
</div>
<div class="abs social" aria-label="Social links"><span></span><span></span><span></span><span></span><span></span></div>
<div class="abs copy">Copyright Velmorra 2012</div>
</body>
</html>
```